Garage Door Service Business Full Truck Wrap

I need a “billboard” on my truck. I would like a wrap that displays my company name, logo, phone number, website, and what we do, services we offer, and areas we service. while it is a lot of information, Im looking for eye catching or a “wow factor” something that stands out. My primary business color scheme is black and gold Information listed below:

Lumen Garage Doors and Hinges
(804) 555-2947

www.lumenoverheadportals.example

Serving Hampton Roads, Richmond, and surrounding counties

Residential Garage Door Experts

Same Day & 24/7 Emergency Service

2023 silverado 1500

Target Market(s)

residential garage door service

Industry/Entity Type

Garage Door Repair and Installation

Font styles to use
Serif

Requirements
Must have
• Business Name, Phone, Website
Nice to have
• Services Offered and Locations Serviced

```html
<!DOCTYPE html>
<html lang="en">
<head>
<meta charset="utf-8">
<title>Lumen Garage Doors and Hinges — Truck Wrap</title>
<link href="https://fonts.googleapis.com/css2?family=Open+Sans:wght@600;700&display=swap" rel="stylesheet">
<style>
  :root {
    --wrap-black: #0b0a08;
    --gold: #c9a24a;
    --gold-deep: #8a6a25;
    --white: #ffffff;
    --paint: #f4f4f2;
  }
  html, body {
    margin: 0;
    padding: 0;
    width: 1200px;
    height: 582px;
    overflow: hidden;
    background: var(--paint);
  }
  .wrap-canvas {
    display: block;
    width: 1200px;
    height: 582px;
  }
  .band { fill: var(--wrap-black); }
  .gold-stripe { fill: var(--gold); }
  .business-name, .website, .phone, .tagline, .service-area, .service-area-sub, .legal-name, .badge-text {
    font-family: "Open Sans", sans-serif;
  }
  .business-name { font-weight: 700; font-size: 31px; fill: var(--gold); }
  .website { font-weight: 700; font-size: 16px; fill: var(--white); }
  .phone { font-weight: 700; font-size: 27px; fill: var(--gold); }
  .tagline { font-weight: 700; font-size: 20px; fill: var(--gold); }
  .service-area { font-weight: 700; font-size: 16px; fill: var(--gold); }
  .service-area-sub { font-weight: 600; font-size: 12px; fill: var(--gold); }
  .legal-name { font-weight: 600; font-size: 12.5px; fill: var(--white); }
  .badge-burst { fill: var(--gold); stroke: var(--gold-deep); stroke-width: 1.5; }
  .badge-text { font-weight: 700; fill: var(--wrap-black); text-anchor: middle; }
  .icon-line { fill: none; stroke: var(--white); stroke-width: 1.6; }
  .icon-gold { fill: var(--gold); }
</style>
</head>
<body>
<svg class="wrap-canvas" viewBox="0 0 1200 582" xmlns="http://www.w3.org/2000/svg">
  <defs>
    <radialGradient id="emblemTone" cx="50%" cy="50%" r="50%">
      <stop offset="0%" stop-color="#c9a24a" stop-opacity="0.55"/>
      <stop offset="100%" stop-color="#c9a24a" stop-opacity="0"/>
    </radialGradient>
  </defs>

  <g class="wrap-layout" transform="rotate(-6 600 291)">
    <rect class="gold-stripe" x="-200" y="180" width="1600" height="6"/>
    <rect class="band" x="-200" y="190" width="1600" height="220"/>
    <rect class="gold-stripe" x="-200" y="412" width="1600" height="5"/>

    <ellipse role="img" aria-label="Gold laurel wreath emblem" cx="420" cy="310" rx="80" ry="80" fill="url(#emblemTone)"/>

    <g class="website-line">
      <circle class="icon-line" cx="530" cy="219" r="8"/>
      <ellipse class="icon-line" cx="530" cy="219" rx="3.5" ry="8"/>
      <line class="icon-line" x1="522" y1="219" x2="538" y2="219"/>
      <text class="website" x="545" y="225">www.lumenoverheadportals.example</text>
    </g>

    <text class="business-name" x="522" y="290">Lumen Garage Doors and Hinges</text>

    <g class="phone-line">
      <circle class="icon-gold" cx="535" cy="345" r="11"/>
      <path d="M530 339 q-2 6 4 11 q3 2 6 1 l-1-3 -3 0 q-3-2-4-5 l1-2z" fill="#0b0a08"/>
      <text class="phone" x="552" y="355">(804) 555-2947</text>
    </g>

    <text class="legal-name" x="540" y="388">Lumen Garage Doors and Hinges</text>

    <text class="tagline" x="772" y="340">Residential Garage</text>
    <text class="tagline" x="800" y="366">Door Experts</text>

    <text class="service-area" x="872" y="232">Serving Hampton Roads, Richmond</text>
    <text class="service-area-sub" x="960" y="250">and surrounding counties</text>

    <g class="emergency-badge" transform="translate(1098 330)">
      <polygon class="badge-burst" points="0,-48 10,-36 24,-42 26,-27 41,-24 35,-10 46,0 35,10 41,24 26,27 24,42 10,36 0,48 -10,36 -24,42 -26,27 -41,24 -35,10 -46,0 -35,-10 -41,-24 -26,-27 -24,-42 -10,-36"/>
      <text class="badge-text" x="0" y="-6" font-size="22">24/7</text>
      <text class="badge-text" x="0" y="10" font-size="10.5">Emergency</text>
      <text class="badge-text" x="0" y="23" font-size="10.5">Service</text>
    </g>
  </g>
</svg>
</body>
</html>
```